PLUM BUSINESS CARD

Need a business card and logo. The company name is PLUM (Piedmont League of Ultimate Mareriders). It's a business that offers horseback riding lessons to young girls. Please put my name: Renata Bowley and a place for email and phone number. I would like the card to look feminine and soft. I like script type lettering. I want the card to be white or ivory with black or gray and hot pink print. A horse head outline would be cool, something whimsical. Think teen girl who likes glamour. Also, I give western riding lessons. So I like faded out background Images of western saddles, cowgirls, horses with long hair, ropes, horses in sunset...mabe the word PLUM can be made out of a lasso rope?

Just updated my project with a little more detail

Target Market(s)

Young girls/ cowgirls, western riding

Industry/Entity Type

Horseback Riding

Font styles to use
Script

Colors
e34197

Requirements
Must have
• A logo of PLUM.
Must say Piedmont League of Ultimate Mareriders
Colors are Pink and Black with an elegant, glamorous, feminine look.
Nice to have
• Could have a picture or outline of a horse

```html
<!DOCTYPE html>
<html lang="en">
<head>
<meta charset="utf-8">
<title>PLUM Business Card</title>
<link rel="stylesheet" href="https://fonts.googleapis.com/css2?family=Kaushan+Script&family=Questrial&display=swap">
<style>
  :root {
    --page-bg: #f1eef0;
    --plum-deep: #2a0620;
    --plum-dark: #5a0f42;
    --plum-mid: #9a2470;
    --hot-pink: #e34197;
    --pink-soft: #f6a6d4;
    --pink-glow: #ffd6ee;
    --ink-white: #ffffff;
    --ink-shadow: rgba(30, 0, 20, 0.75);
  }
  * { margin: 0; padding: 0; box-sizing: border-box; }
  html, body {
    width: 1200px;
    height: 900px;
    overflow: hidden;
    background: var(--page-bg);
  }
  .canvas {
    position: relative;
    width: 1200px;
    height: 900px;
  }
  .business-card {
    position: absolute;
    left: 100px;
    top: 165px;
    width: 1000px;
    height: 570px;
    overflow: hidden;
    box-shadow: 0 18px 40px rgba(0, 0, 0, 0.25);
  }
  .card-photo {
    position: absolute;
    inset: 0;
    background:
      radial-gradient(ellipse 40% 45% at 88% 8%, var(--pink-glow) 0%, rgba(255, 214, 238, 0) 70%),
      radial-gradient(ellipse 30% 55% at 68% 48%, rgba(246, 166, 212, 0.55) 0%, rgba(246, 166, 212, 0) 70%),
      linear-gradient(180deg, rgba(42, 6, 32, 0) 45%, rgba(227, 65, 151, 0.55) 80%, rgba(246, 166, 212, 0.7) 100%),
      linear-gradient(100deg, var(--plum-deep) 0%, var(--plum-dark) 35%, var(--plum-mid) 75%, var(--hot-pink) 100%);
  }
  .brand-name {
    position: absolute;
    left: 52px;
    top: 58px;
    font-family: "Questrial", sans-serif;
    font-size: 150px;
    line-height: 1;
    letter-spacing: 6px;
    color: var(--pink-soft);
  }
  .contact {
    position: absolute;
    left: 95px;
    top: 268px;
    color: var(--ink-white);
    text-shadow: 0 2px 4px var(--ink-shadow);
  }
  .contact-name {
    font-family: "Kaushan Script", cursive;
    font-size: 36px;
    line-height: 1.15;
    margin-bottom: 6px;
  }
  .contact-line {
    font-family: "Questrial", sans-serif;
    font-size: 31px;
    line-height: 1.35;
  }
  .league-name {
    position: absolute;
    left: 55px;
    top: 432px;
    font-family: "Kaushan Script", cursive;
    font-size: 35px;
    color: var(--ink-white);
    text-shadow: 0 2px 4px var(--ink-shadow);
    white-space: nowrap;
  }
</style>
</head>
<body>
  <main class="canvas">
    <section class="business-card">
      <div class="card-photo" role="img" aria-label="Pink-toned photograph of a long-maned horse running through a sunlit meadow"></div>
      <div class="brand-name">PLUM</div>
      <div class="contact">
        <p class="contact-name">Renata Bowley</p>
        <p class="contact-line">1704 555 318</p>
        <p class="contact-line">renata@plumriders.com</p>
      </div>
      <p class="league-name">Piedmont League of Ultimate Mareriders</p>
    </section>
  </main>
</body>
</html>
```